Flyer-Design für Kindertagesstätte
Helmsteds Kinderhafen suchte ein neues Design in der Kategorie Flyer und hat ein Projekt auf grafikfinden.de gestartet.
Zielgruppe
Wir sind eine Kindertagesstätte und wollen eine Baby-Kind-Spielgruppe jeden Mittwoch in unserer Kita von 09.00 Uhr bis 11.00 Uhr anbieten.
Aufgabenstellung
Unser LOGO muss im Flyer enthalten sein, auf jeden Fall ein Bild wenn möglich mit mehreren Babys/Kleinkindern bis 1,5 Jahre. Wir benötigen den Flyer in DIN lang - bunt - 1 seitig.
Folgender Text sollte enthalten: Baby-Kind-Spielgruppe, jeden mittwoch in unserer Kita 'Helmsteds Kinderhafen' von 09.00 Uhr bis 11.00 Uhr. Die Spielgruppe wird durch unser ausgebildetes Fachpersonal begleitet.

```html
<!DOCTYPE html>
<html lang="de">
<head>
<meta charset="utf-8">
<title>Baby-Kind-Spielgruppe – Helmsteds Kinderhafen</title>
<link rel="stylesheet" href="https://fonts.googleapis.com/css2?family=Poppins:wght@400;600;700&family=Sriracha&display=swap">
<style>
  :root{
    --stage:#e9e9ea;
    --purple-top:#463b8a;
    --purple-bottom:#6d63b3;
    --lavender:#d9d5f2;
    --yellow:#f7d21c;
    --pink:#ea6a9e;
    --pink-dark:#dc5790;
    --navy:#27233f;
    --white:#ffffff;
    --brown:#5a1f14;
    --blue:#3aa6e0;
    --green:#4cb848;
  }
  *{box-sizing:border-box;margin:0;padding:0}
  html,body{width:1200px;height:684px;overflow:hidden;background:var(--stage)}
  .flyer{
    position:absolute;left:96px;top:114px;width:985px;height:469px;overflow:hidden;
    background:linear-gradient(180deg,var(--purple-top) 0%,var(--purple-bottom) 55%,#655ba9 100%);
    font-family:"Poppins",sans-serif;color:var(--white);
  }
  .layer{position:absolute;left:0;top:0}
  .headline{
    position:absolute;left:395px;top:28px;width:580px;text-align:center;white-space:nowrap;
    font-family:"Sriracha",cursive;font-weight:400;font-size:31px;line-height:46px;color:var(--yellow);
  }
  .subline{position:absolute;left:420px;top:185px;width:540px;text-align:center;white-space:nowrap;font-size:12.5px;font-weight:600}
  .contact-band{
    position:absolute;left:409px;top:240px;width:450px;height:137px;
    background:linear-gradient(180deg,var(--pink) 0%,var(--pink-dark) 100%);
  }
  .contact{position:absolute;left:440px;top:255px;width:380px;text-align:center;white-space:nowrap}
  .contact-lead{font-size:13px;font-weight:700;line-height:22px}
  .contact-phone{font-size:43px;font-weight:700;color:var(--navy);line-height:46px;letter-spacing:0.3px}
  .contact-or{display:flex;align-items:center;gap:8px;justify-content:center;font-size:12.5px;line-height:18px}
  .contact-or::before,.contact-or::after{content:"";width:125px;height:1px;background:rgba(255,255,255,.85)}
  .contact-web{font-size:18px;font-weight:700;color:var(--navy);line-height:28px}
  .note{
    position:absolute;left:405px;top:425px;width:380px;display:flex;align-items:center;justify-content:center;gap:9px;
    font-size:14px;font-weight:600;white-space:nowrap;
  }
  .note-dot{width:22px;height:22px;border-radius:50%;background:var(--white);flex:none}
  .logo{position:absolute;left:812px;top:330px;width:170px;text-align:center;color:var(--brown)}
  .logo-mark{width:22px;height:22px;border-radius:50%;background:var(--brown);margin:0 auto 10px}
  .logo-name{font-size:17px;font-weight:700;line-height:21px}
</style>
</head>
<body>
<main class="flyer">
  <svg class="layer decor" width="985" height="469" aria-hidden="true">
    <line x1="51" y1="0" x2="51" y2="60" stroke="#fff" stroke-width="1"/>
    <path d="M29 38 a8 8 0 0 1 12 -8 a12 12 0 0 1 22 2 a8 8 0 0 1 22 6 z" fill="#fff"/>
    <circle cx="51" cy="75" r="15" fill="var(--yellow)"/>
    <line x1="145" y1="0" x2="145" y2="82" stroke="#fff" stroke-width="1" opacity=".7"/>
    <path d="M145 80 l4 9 l10 1 l-7 7 l2 10 l-9 -5 l-9 5 l2 -10 l-7 -7 l10 -1 z" fill="var(--green)"/>
    <path d="M18 80 l3 7 l8 1 l-6 5 l2 8 l-7 -4 l-7 4 l2 -8 l-6 -5 l8 -1 z" fill="var(--lavender)"/>
    <path d="M221 16 l2 5 l6 1 l-4 4 l1 6 l-5 -3 l-5 3 l1 -6 l-4 -4 l6 -1 z" fill="var(--lavender)"/>
    <circle cx="80" cy="58" r="3" fill="var(--lavender)"/>
    <circle cx="380" cy="104" r="3" fill="var(--lavender)"/>
    <circle cx="347" cy="37" r="6" fill="none" stroke="var(--yellow)" stroke-width="3"/>
    <line x1="374" y1="0" x2="374" y2="40" stroke="var(--blue)" stroke-width="1"/>
    <path d="M378 40 l-10 16 h8 l-6 14 l14 -18 h-8 l6 -12 z" fill="var(--blue)"/>
    <path d="M921 160 l28 -4 l-14 24 l-4 -11 z" fill="#fff" opacity=".9"/>
    <circle cx="539" cy="404" r="8" fill="none" stroke="var(--pink)" stroke-width="3"/>
    <circle cx="594" cy="395" r="5" fill="none" stroke="var(--yellow)" stroke-width="3"/>
    <circle cx="364" cy="440" r="11" fill="var(--yellow)"/>
    <circle cx="34" cy="407" r="12" fill="none" stroke="var(--pink)" stroke-width="4"/>
    <path d="M0 445 a22 22 0 0 1 26 -6 a18 18 0 0 1 16 30 h-42 z" fill="var(--yellow)"/>
  </svg>

  <svg class="layer photo-frame" width="985" height="469" role="img" aria-label="Foto: zwei Kleinkinder spielen im Gruppenraum mit bunten Stapelringen">
    <defs>
      <linearGradient id="photoTone" gradientUnits="userSpaceOnUse" x1="0" y1="30" x2="430" y2="460">
        <stop offset="0" stop-color="#e8cfa0"/>
        <stop offset=".5" stop-color="#d8bcae"/>
        <stop offset="1" stop-color="#c7a99c"/>
      </linearGradient>
    </defs>
    <g fill="var(--lavender)">
      <circle cx="214" cy="246" r="150"/>
      <circle cx="344" cy="246" r="88"/><circle cx="279" cy="359" r="88"/><circle cx="149" cy="359" r="88"/>
      <circle cx="84" cy="246" r="88"/><circle cx="149" cy="133" r="88"/><circle cx="279" cy="133" r="88"/>
    </g>
    <g fill="url(#photoTone)">
      <circle cx="214" cy="246" r="136"/>
      <circle cx="340" cy="246" r="74"/><circle cx="277" cy="355" r="74"/><circle cx="151" cy="355" r="74"/>
      <circle cx="88" cy="246" r="74"/><circle cx="151" cy="137" r="74"/><circle cx="277" cy="137" r="74"/>
    </g>
  </svg>

  <h1 class="headline">Baby-Kind-Spielgruppe, jeden mittwoch<br>in unserer Kita 'Helmsteds Kinderhafen'<br>von 09.00 Uhr bis 11.00 Uhr.</h1>
  <p class="subline">Die Spielgruppe wird durch unser ausgebildetes Fachpersonal begleitet.</p>

  <div class="contact-band"></div>
  <div class="contact">
    <p class="contact-lead">Voranmeldungen bitte unter telefonisch unter:</p>
    <p class="contact-phone">0351-4827160</p>
    <p class="contact-or">oder unter</p>
    <p class="contact-web">www.helmsteds-kinderhafen.de</p>
  </div>

  <p class="note"><span class="note-dot"></span>Spielgruppe ist öffentlich und kostenfrei.<span class="note-dot"></span></p>

  <svg class="layer logo-cloud" width="985" height="469" aria-hidden="true">
    <g fill="#fff">
      <circle cx="900" cy="340" r="105"/>
      <circle cx="950" cy="250" r="55"/>
      <circle cx="835" cy="410" r="65"/>
      <rect x="900" y="250" width="85" height="219"/>
      <rect x="835" y="380" width="150" height="89"/>
    </g>
  </svg>
  <div class="logo">
    <div class="logo-mark"></div>
    <p class="logo-name">Helmsteds<br>Kinderhafen</p>
  </div>
</main>
</body>
</html>
```